Varodel ApS cool new identity on web
Free your mind for the perfect look
Information Technology
www.varodel-example.dk
Varodel offers hosted technologies, and is one of the frontrunners and cutting edge partners for companies within webservices, and security solutions for network solutions.
1. website standard informations site, front website or other standard information sites regarding services or the company
2. website sample with eg. contact form or other types of forms, or a standard site with integrated form to contact, download information etc..
3. product login / portal site, eg. portal where clients login to on central portal with option to choose wich service they want to edit or adapt changes to - eg. our video or postsift systems with options to release mails, upload videos etc..
green
white and sand
top
www.brakvinhost.example
www.olafkestrup.example
www.qev.example
We want the design to show trust, technology, to be frontrunner, inovation etc. - streamlined with a crisp look.
Visual effects etc. are welcome to assist text, function, design and visuality.
Other website design that look interesting - however we don´t want a standard template - it´s important that we don´t look like "the others"
http://www.layoutpantry.example/website-templates/19964.html
http://www.layoutpantry.example/website-templates/19207.html
http://www.layoutpantry.example/website-templates/35125.html
http://www.layoutpantry.example/website-templates/35287.html
http://www.layoutpantry.example/website-templates/35041.html
http://www.layoutpantry.example/website-templates/34857.html
Draft of our selected stationary etc
List interface

```html
<!DOCTYPE html>
<html lang="en">
<head>
<meta charset="utf-8">
<title>Varodel ApS</title>
<link href="https://fonts.googleapis.com/css2?family=Arimo:wght@400;700&display=swap" rel="stylesheet">
<style>
:root{
  --green:#8dc63f;
  --green-dark:#5e9a1c;
  --ink:#222;
  --grey-text:#555;
  --page-dark:#1d1e1f;
  --page-mid:#2c2d2e;
  --panel:#f3f3f1;
  --nav:#dcdcda;
  --footer:#ececea;
  --white:#fff;
}
*{box-sizing:border-box;margin:0;padding:0}
html,body{width:1200px;height:845px;overflow:hidden}
body{position:relative;font-family:"Arimo",Arial,sans-serif;color:var(--ink);
  background:linear-gradient(180deg,var(--page-dark) 0,var(--page-mid) 50%,#3a3b3c 88%);}
.abs{position:absolute}

/* header */
.brand{left:180px;top:22px}
.brand-name{font-weight:700;font-size:44px;line-height:48px;color:var(--white);letter-spacing:-.5px}
.top-links{right:200px;top:16px;font-size:12px;color:#ccc;white-space:nowrap}
.top-links span{margin:0 5px;color:#888}
.search{left:775px;top:40px;width:257px;height:24px;border-bottom:3px solid var(--green)}
.search-icon{left:1002px;top:40px}

/* nav */
.navbar{left:149px;top:89px;width:888px;height:43px;background:linear-gradient(#f0f0ee,var(--nav));border-radius:6px 6px 0 0;display:flex;align-items:center;white-space:nowrap}
.social{display:flex;gap:6px;margin-left:16px}
.social i{display:block;width:22px;height:22px;border-radius:4px}
.stat{font-size:10px;color:#777;margin-left:14px}
.nav-links{display:flex;margin-left:auto;height:100%}
.nav-links a{display:flex;align-items:center;padding:0 16px;font-size:13px;font-weight:700;color:#333;text-decoration:none;border-left:1px solid #bbb}

/* hero */
.hero{left:149px;top:132px;width:888px;height:307px;background:radial-gradient(ellipse at 65% 45%,#c9cccd 0,#8a8e90 35%,#3e4244 70%,#1c1e1f 100%)}
.signup{left:163px;top:149px;width:240px;height:230px;background:rgba(30,32,33,.86);border-radius:6px;color:#ddd;padding:14px 14px}
.signup h2{font-size:17px;color:var(--white);padding-bottom:8px;border-bottom:3px solid var(--green);margin:-2px -14px 10px;padding-left:14px}
.signup p{font-size:11px;line-height:1.45;margin-bottom:10px}
.signup label{display:block;font-size:11px;margin-bottom:4px}
.signup .field{height:26px;background:#3b3d3e;border:1px solid #555;margin-bottom:12px}
.btn{display:inline-block;background:linear-gradient(#b6e26a,var(--green-dark));color:#102;font-weight:700;font-size:13px;padding:5px 22px;border-radius:4px;white-space:nowrap}
.signup .btn{margin-left:94px}
.caption{left:490px;top:338px;width:547px;height:80px;background:rgba(20,20,20,.55);padding:12px 14px;color:#ccc}
.caption h3{color:var(--green);font-size:22px;font-weight:400;margin-bottom:6px}
.caption p{font-size:11px;line-height:1.45}
.dots{left:300px;top:408px;display:flex;gap:10px}
.dots i{width:11px;height:11px;border-radius:50%;background:#777}
.dots i:first-child{background:var(--green)}
.hero-band{left:149px;top:439px;width:888px;height:17px;background:#4a4b4c;border-bottom:7px solid var(--green)}

/* content */
.content{left:149px;top:456px;width:888px;height:285px;background:linear-gradient(#fafaf8,var(--panel))}
.pdf-art{left:163px;top:466px;width:100px;height:96px;background:linear-gradient(135deg,#cfd0d0,#6a6c6d);border-radius:4px}
.brochure{left:283px;top:494px;width:450px}
.brochure h3{font-size:15px;color:#333;margin-bottom:6px}
.brochure p{font-size:11px;color:var(--grey-text);line-height:1.45}
.brochure em{color:#e07b00;font-style:normal}
.newsletter{left:763px;top:482px;width:260px;height:92px;background:#d3d3d1;border-radius:5px}
.newsletter h3{font-size:14px;color:#444;padding:9px 10px;border-bottom:1px solid #bbb}
.newsletter .row{display:flex;gap:6px;padding:12px 10px}
.newsletter .input{flex:1;height:24px;background:#555;border-radius:3px}
.newsletter .btn{font-size:11px;padding:4px 10px}
.feature{top:598px;width:262px}
.feature .icon{position:absolute;left:0;top:4px;width:54px;height:54px;border-radius:6px;background:linear-gradient(#e2e2e2,#8d8f90)}
.feature .body{margin-left:66px}
.feature h4{font-size:14px;margin-bottom:6px;white-space:nowrap}
.feature p{font-size:10.5px;line-height:1.45;color:var(--grey-text);margin-bottom:8px}
.feature .btn{font-size:11px;padding:4px 14px;border-radius:10px;margin-left:-66px;background:linear-gradient(#a6d65a,var(--green-dark));color:#fff}
.content-band{left:149px;top:733px;width:888px;height:7px;background:var(--green)}

/* footer */
.footer{left:0;top:744px;width:1200px;height:101px;background:var(--footer)}
.footer-links{left:163px;top:762px;font-size:11px;color:#444;white-space:nowrap}
.footer-links span{margin:0 5px;color:#999}
.copyright{left:163px;top:810px;font-size:10px;color:#999}
.contact{left:876px;top:760px;font-size:11px;line-height:1.5;color:#333;white-space:nowrap}
</style>
</head>
<body>
<header>
  <div class="abs brand"><div class="brand-name">Varodel</div></div>
  <div class="abs top-links">Log in<span>|</span>Sign up<span>|</span>Customer Support</div>
  <div class="abs search"></div>
  <svg class="abs search-icon" width="22" height="22" viewBox="0 0 22 22"><circle cx="9" cy="9" r="6" fill="none" stroke="#8dc63f" stroke-width="3"/><line x1="13.5" y1="13.5" x2="20" y2="20" stroke="#8dc63f" stroke-width="3"/></svg>
  <nav class="abs navbar">
    <div class="social"><i style="background:#f08a24"></i><i style="background:#3b5998"></i><i style="background:#3fb4e6"></i></div>
    <span class="stat">256,120 Followers</span>
    <span class="stat">98,120 Page Fans</span>
    <div class="nav-links">
      <a href="#">Home</a><a href="#">About us</a><a href="#">Services</a><a href="#">Products</a><a href="#">Help Center</a><a href="#">Contact Us</a>
    </div>
  </nav>
</header>

<section>
  <div class="abs hero" role="img" aria-label="Photo of steel chain links lying on a computer keyboard"></div>
  <form class="abs signup">
    <h2>Sign up</h2>
    <p>Lorem ipsum dolor sit amet, consectetur adipiscing metus.</p>
    <label>E-mail address</label><div class="field"></div>
    <label>Full Name</label><div class="field"></div>
    <span class="btn">Sign up</span>
  </form>
  <div class="abs caption">
    <h3>Network Security</h3>
    <p>Curabitur et erat et ipsum dignissim tempor. Morbi lorem elit, elementum vel porta eget, elementum quis magna. Fusce a mauris ut turpis scelerisque fringilla quis sed dui.</p>
  </div>
  <div class="abs dots"><i></i><i></i><i></i><i></i></div>
  <div class="abs hero-band"></div>
</section>

<main>
  <div class="abs content"></div>
  <div class="abs pdf-art" role="img" aria-label="Illustration of a chip labelled as a PDF brochure"></div>
  <div class="abs brochure">
    <h3>Download Varodel ApS Brochure</h3>
    <p>Pellentesque eu lectus, fermentum id ultrices ac, ultrices eu nulla. Maecenas accumsan accumsan dui ut rhoncus. Morbi nec ligula ante, ut faucibus orci. <em>Download here</em></p>
  </div>
  <div class="abs newsletter">
    <h3>Subscribe to our Newsletter</h3>
    <div class="row"><div class="input"></div><span class="btn">Submit</span></div>
  </div>

  <div class="abs feature" style="left:163px">
    <div class="icon" role="img" aria-label="Network server icon"></div>
    <div class="body">
      <h4>Network Solutions</h4>
      <p>Lorem ipsum dolor sit amet, consectetur adipiscing elit. Nunc vitae purus velit. Suspendisse id dolor placerat tortor fringilla egestas condimentum.</p>
      <span class="btn">Read more</span>
    </div>
  </div>
  <div class="abs feature" style="left:463px">
    <div class="icon" role="img" aria-label="Web services database icon"></div>
    <div class="body">
      <h4>Web Services</h4>
      <p>Lorem ipsum dolor sit amet, consectetur adipiscing elit. Nunc vitae purus velit. Suspendisse id dolor placerat tortor fringilla egestas condimentum.</p>
      <span class="btn">Read more</span>
    </div>
  </div>
  <div class="abs feature" style="left:763px">
    <div class="icon" role="img" aria-label="Security solutions monitor icon"></div>
    <div class="body">
      <h4>Security Solutions</h4>
      <p>Lorem ipsum dolor sit amet, consectetur adipiscing elit. Nunc vitae purus velit. Suspendisse id dolor placerat tortor fringilla egestas condimentum.</p>
      <span class="btn">Read more</span>
    </div>
  </div>
  <div class="abs content-band"></div>
</main>

<footer>
  <div class="abs footer"></div>
  <div class="abs footer-links">Site Map<span>|</span>Services<span>|</span>About Us<span>|</span>Terms &amp; Conditions<span>|</span>Privacy Policy<span>|</span>Blog<span>|</span>Contact Us</div>
  <div class="abs copyright">© 2011 Varodel ApS. All rights reserved.</div>
  <div class="abs contact">
    Phone Number +45 20 00 01 99<br>
    Fax Number (00) 00 000<br>
    E-mail info@varodel-example.dk<br>
    Address Denmark
  </div>
</footer>
</body>
</html>
```